B2B modern industry lubrication label

We are a chemical company that needs a new, very modern outstanding lubrication packaging label. The logo attached can be changed in color. The name of the product is R83. Attached also the text you can use, please disregard the current layout of the text, you can make it any layout you want. Be free in font type, colors and other design aspects.
Dimensions: 21 x 14,8 cm
Target Market(s)
industry, companies with machinery
Industry/Entity Type
Industrial
Colors
Designer to choose colors to be used in the design.
Look and feel
Each slider illustrates characteristics of the customer's brand and the style your logo design should communicate.

```html
<!DOCTYPE html>
<html lang="en">
<head>
<meta charset="utf-8">
<title>R83 Pro Lubricant Label</title>
<link rel="stylesheet" href="https://fonts.googleapis.com/css2?family=Lilita+One&family=Montserrat:wght@500;700;800&display=swap">
<style>
  :root {
    --bg: #e6e6e6;
    --yellow-base: #c9c100;
    --yellow-light: #e4da00;
    --yellow-dark: #aea600;
    --ink: #0b0b0b;
    --cap-white: #eeeeee;
    --brand-orange: #d8521c;
  }
  html, body {
    margin: 0;
    width: 1200px;
    height: 1200px;
    overflow: hidden;
    background: var(--bg);
  }
  .label {
    position: absolute;
    left: 452px;
    top: 230px;
    width: 268px;
    height: 900px;
    overflow: hidden;
    background: var(--yellow-base);
  }
  .label-stripes {
    position: absolute;
    inset: 0;
  }
  .brand-band {
    position: absolute;
    left: 0;
    top: 0;
    width: 268px;
    height: 150px;
  }
  .brand-name {
    position: absolute;
    left: 0;
    width: 268px;
    top: 40px;
    text-align: center;
    font-family: "Montserrat", sans-serif;
    font-weight: 800;
    font-size: 42px;
    letter-spacing: 0;
    color: var(--brand-orange);
  }
  .product-code span {
    position: absolute;
    font-family: "Lilita One", sans-serif;
    color: var(--ink);
    line-height: 1;
  }
  .code-r { left: 38px; top: 150px; font-size: 300px; }
  .code-8 { left: 34px; top: 380px; font-size: 220px; }
  .code-3 { left: 88px; top: 470px; font-size: 280px; }
  .tier {
    position: absolute;
    left: 170px;
    top: 400px;
    font-family: "Montserrat", sans-serif;
    font-weight: 800;
    font-size: 27px;
    color: var(--ink);
  }
  .variant, .specs {
    position: absolute;
    left: 0;
    width: 268px;
    text-align: center;
    font-family: "Montserrat", sans-serif;
    color: #1c1c10;
  }
  .variant { top: 806px; font-size: 18px; font-weight: 500; letter-spacing: 1px; }
  .specs { top: 844px; font-size: 13px; font-weight: 500; line-height: 1.25; letter-spacing: 0.5px; }
</style>
</head>
<body>
  <main class="label">
    <svg class="label-stripes" width="268" height="900" viewBox="0 0 268 900">
      <polygon points="0,330 268,130 268,330 0,560" fill="var(--yellow-light)"/>
      <polygon points="0,560 268,330 268,430 0,700" fill="#dcd200"/>
      <polygon points="0,700 268,430 268,900 0,900" fill="var(--yellow-dark)" opacity="0.55"/>
      <polygon points="0,150 100,150 0,260" fill="var(--yellow-dark)" opacity="0.5"/>
    </svg>
    <svg class="brand-band" width="268" height="150" viewBox="0 0 268 150">
      <path d="M0,0 H268 V55 C220,150 48,150 0,75 Z" fill="var(--cap-white)"/>
    </svg>
    <div class="brand-name">KESTRA</div>
    <div class="product-code" aria-label="R83">
      <span class="code-r">R</span>
      <span class="code-8">8</span>
      <span class="code-3">3</span>
    </div>
    <div class="tier">PRO</div>
    <div class="variant">YELLOW</div>
    <div class="specs">1.07 G/ML<br>-40 UNTIL 370°C</div>
  </main>
</body>
</html>
```